Alcohol Marketing website

Home page and information page design, details as follows

CLIENT PURPOSE
Increase online visibility and create good contacts to increase business.

SERVICES
Drinks Marketing Consultancy
Brand Representation
Spirit Brand Sales & Marketing
Brand Development
Brand Distribution
Brand Launch & Introductions

COMPETITION
hazelpour.co.uk -
quintaloft.co.uk -

WEBSITE(S) CLIENT LIKES
Small competitors I admire:
http://www.hazelpour.co.uk/main.htm
http://www.quintaloft.com
http://www.morvatide.co.uk/spiritsliqueursbybrand.php
http://www.kelbrowhouse.com/page1.html
http://www.quorrifenwave.co.uk/index.asp

Nice page layout:
http://www.nkplume.com/
http://www.wzoharbour.com/
http://www.pelvit.com/index.cfm?do=pelvit.home

WEBSITE CLIENT DOES NOT LIKE
http://www.corvanhall.com/
http://www.amberlode-hall.com/
http://www.thesupperfold.co.uk/aboutUs.html
http://www.grainandkettle.com/
http://www.tessmarrow.co.uk/default.asp
http://www.pinnock-halden.co.uk/start.htm
http://www.rilby.co.uk/
http://www.vmkettles.com/default2.aspx
http://www.tumbril-vale.co.uk/mainpage.aspx

COMPANY LOGO
Customer has a company logo (Supplied)

COLOURS:
Blue
White

STRAPLINE:
No

WEBSITE THEME: Marketing

IMAGES THAT BEST REFLECT THE COMPANY:
Spirits / Drinks

HEADER IMAGE:
Spirits / Brands

PAGES:
home
strength& flavour
a little about us
our spirit marketing
big brand success
speak to us

USER JOURNEYS:
General Service > Land on website >Navigation > Info Pages > Contact Form
Questions > Land on website > Message Banners > Info Pages > Contact Form
Contact > Land on website > Clear Telephone / Email Banner > Contact Form

CALL TO ACTION BANNER:
If you need help making your drink the next big brand, speak to us today.

KEYWORDS THAT RELATE TO THE BUSINESS:
brand marketing
drinks marketing
spirits marketing
brand marketing strategy
alcoholic drinks marketing
Drinks Brand Development

LOCATION(S):
United Kingdom -
Worldwide -

Target Market(s)

Male & Female
30-60
Marketing Directors
Brand Developers
Export Directors
Brand Managers

Industry/Entity Type

Marketing

Number of Pages Required

2 pages

Requirements
Must have
• This design will be integrated into wordpress, I have attached a wireframe of what we need, this is NOT a strict guide but contains content that is essential, the wireframes shows the priority of statements and products. the images supplied need to sell the products and services.
The main banner will eventually be animated so this needs to be taken into account.
The cliemt has supplied images which will need to be used in the design , however if you feel you have better images in the same style then they can be used.
Nice to have
• animation included, Jquery
Should not have
• NO fully flash sites or designs, this site will be Search engine optimised and updateable

```html
<!DOCTYPE html>
<html lang="en">
<head>
<meta charset="utf-8">
<title>a little about us – Proof &amp; Palate</title>
<link rel="stylesheet" href="https://fonts.googleapis.com/css2?family=Arimo:ital,wght@0,400;0,700;1,400;1,700&display=swap">
<style>
  :root {
    --brand-blue: #0a4d98;
    --sky-top: #bfe4f7;
    --sky-mid: #e6f5fc;
    --accent-cyan: #1aa3d9;
    --text: #5a5a5a;
    --text-dark: #3c3c3c;
    --muted: #8e8e8e;
    --nav-bg: #f5f5f5;
    --nav-line: #d9d9d9;
    --tab-active: #b9bec3;
    --rule: #cfcfcf;
    --white: #ffffff;
  }
  * { margin: 0; padding: 0; box-sizing: border-box; }
  html, body { width: 1154px; height: 1200px; overflow: hidden; }
  body {
    position: relative;
    background: var(--white);
    font-family: "Arimo", Arial, sans-serif;
    color: var(--text);
  }

  .site-header {
    position: absolute; left: 0; top: 0; width: 1154px; height: 187px;
    background: linear-gradient(180deg, var(--sky-top) 0%, var(--sky-mid) 45%, var(--white) 80%);
  }
  .brand-name {
    position: absolute; left: 0; top: 42px; width: 1154px; text-align: center;
    font-size: 21px; font-weight: 700; letter-spacing: 0.5px; color: var(--text-dark);
  }
  .contact {
    position: absolute; left: 830px; top: 128px;
    font-size: 12px; line-height: 15px; color: var(--text);
  }
  .contact b { color: var(--text-dark); }
  .contact .email { text-decoration: underline; }
  .follow { display: flex; align-items: center; gap: 6px; margin-top: 5px; font-weight: 700; font-size: 11px; color: var(--text-dark); }
  .social-square { width: 16px; height: 16px; border-radius: 2px; background: var(--brand-blue); }
  .social-square.light { background: var(--accent-cyan); }

  .main-nav {
    position: absolute; left: 0; top: 187px; width: 1154px; height: 56px;
    background: var(--nav-bg);
    border-top: 1px solid var(--nav-line); border-bottom: 1px solid var(--nav-line);
  }
  .main-nav ul { list-style: none; position: relative; height: 100%; }
  .main-nav li {
    position: absolute; top: 0; height: 54px; line-height: 54px;
    font-size: 16px; color: var(--text);
  }
  .main-nav li.active {
    background: var(--tab-active); color: var(--white); font-weight: 700;
    text-align: center;
  }
  .main-nav li.active::after {
    content: ""; position: absolute; left: 70px; bottom: -8px;
    border-left: 8px solid transparent; border-right: 8px solid transparent;
    border-top: 8px solid var(--tab-active);
  }

  .page-banner {
    position: absolute; left: 0; top: 247px; width: 1154px; height: 94px;
    background: var(--brand-blue);
  }
  .page-banner h1 {
    position: absolute; left: 157px; top: 24px;
    font-size: 40px; font-weight: 700; color: var(--white); letter-spacing: 0.3px;
  }

  .feature-photo {
    position: absolute; left: 126px; top: 371px; width: 269px; height: 424px;
    border: 5px solid #0b0b0b;
    background: linear-gradient(160deg, #3a2016 0%, #8c5a3c 35%, #d9d6cf 55%, #2a2aa0 75%, #5b3a2c 100%);
  }
  .photo-caption {
    position: absolute; left: 147px; top: 803px; width: 220px;
    font-size: 11px; line-height: 14px; font-style: italic; color: #a0a0a0;
  }

  .article {
    position: absolute; left: 425px; top: 368px; width: 606px;
    font-size: 12px; line-height: 17px; color: var(--text); letter-spacing: -0.15px;
  }
  .article .lead { font-weight: 700; font-style: italic; color: var(--text); }
  .article p { margin-bottom: 17px; }
  .article .subhead { font-weight: 700; margin-bottom: 13px; }
  .ticks { list-style: none; margin: 0 0 29px 20px; }
  .ticks li { position: relative; padding-left: 16px; margin-bottom: 13px; }
  .ticks li svg { position: absolute; left: 0; top: 3px; }
  .ticks em { color: var(--text); }

  .highlights { position: absolute; left: 126px; top: 890px; width: 900px; }
  .highlight { position: absolute; top: 0; width: 300px; height: 170px; }
  .highlight .marker { position: absolute; left: 0; top: 4px; }
  .highlight h2 {
    margin-left: 36px; font-size: 25px; line-height: 30px; font-weight: 400;
    color: var(--brand-blue); white-space: nowrap;
  }
  .highlight p {
    margin: 12px 0 0 39px; width: 234px; font-size: 12px; line-height: 17px; color: var(--text);
    letter-spacing: -0.15px;
  }
  .highlight.third p { margin-left: 36px; width: 240px; }
  .read-more {
    position: absolute; top: 149px; width: 99px; height: 20px;
    border: 1px solid #c4c4c4; border-radius: 10px;
    background: linear-gradient(180deg, #fafafa, #dedede);
    font-size: 11px; font-weight: 700; line-height: 18px; color: #666;
    text-align: center;
  }
  .read-more::after {
    content: ""; display: inline-block; margin-left: 5px; vertical-align: 0;
    border-top: 4px solid transparent; border-bottom: 4px solid transparent;
    border-left: 5px solid #555;
  }

  .site-footer {
    position: absolute; left: 126px; top: 1089px; width: 900px;
    border-top: 1px solid var(--rule); text-align: center;
  }
  .keyword-links { margin-top: 18px; font-size: 12px; font-weight: 700; color: #555; }
  .keyword-links span { margin: 0 3px; font-weight: 400; }
  .legal { margin-top: 12px; font-size: 11px; color: #666; }
</style>
</head>
<body>

<header class="site-header">
  <div class="brand-name">PROOF &amp; PALATE</div>
  <div class="contact">
    <div><b>T:</b> 020 7946 0321</div>
    <div><b>E:</b> <span class="email">info@proofandpalate.com</span></div>
    <div class="follow">Follow us: <span class="social-square"></span><span class="social-square light"></span></div>
  </div>
</header>

<nav class="main-nav">
  <ul>
    <li style="left:148px">home</li>
    <li style="left:236px">proof &amp; palate</li>
    <li class="active" style="left:387px;width:156px">a little about us</li>
    <li style="left:564px">our spirit marketing</li>
    <li style="left:747px">big brand success</li>
    <li style="left:924px">speak to us</li>
  </ul>
</nav>

<section class="page-banner">
  <h1>a little about us</h1>
</section>

<div class="feature-photo" role="img" aria-label="Photo of a cocktail in a martini glass with a blue stem, garnished with a physalis, on a bar counter"></div>
<p class="photo-caption">A caption goes here lorem impum dolor sit amet consecterut adispison</p>

<article class="article">
  <p><span class="lead">Lorem ipsum dolor sit amet, consectetur adipiscing elit. Nulla elementum, ligula in porta adipiscing, arcu velit tincidunt nulla, in luctus nisi risus malesuada elit. Mauris interdum justo massa, at pellentesque metus. Morbi dignissim tempor tellus vitae mattis. Vestibulum augue nisl, semper non vulputate imperdiet, commodo sollicitudin lacus</span>. Nam orci massa, faucibus quis lacinia a, tempus at turpis. Pellentesque faucibus felis sed orci sodales ut faucibus arcu iaculis. Nullam in eros risus. Sed varius metus sit amet nibh faucibus pulvinar. Pellentesque habitant morbi tristique senectus et netus et malesuada fames ac turpis egestas. In leo lorem, dapibus ut rutrum eu, tincidunt ut odio. Nulla at mauris vel nisi interdum adipiscing quis at orci. Aliquam ut metus est. Morbi commodo faucibus lorem, et malesuada ante laoreet id. Vestibulum eu ornare orci. Nunc cursus adipiscing augue. Aliquam ultricies lectus ac arcu hendrerit pharetra. Nullam tincidunt tristique mauris sed varius. Proin massa nisi, feugiat at cursus eu, faucibus ut felis. Maecenas ac pretium orci. Suspendisse rutrum condimentum erat in ultricies.</p>
  <p class="subhead">Sed elit magna, accumsan sed varius vel, faucibus sed lectus. Aenean fermentum risus quis ligula feugiat pulvinar.</p>
  <ul class="ticks">
    <li><svg width="11" height="9" viewBox="0 0 11 9"><path d="M1 4.5 L4 7.5 L10 1" fill="none" stroke="#1aa3d9" stroke-width="2.2"/></svg><em>Sed sit amet quam id lorem aliquam facilisis.</em> Nam tincidunt faucibus ligula, id consectetur arcu vulputate eu. Mauris at ante libero, vel pellentesque arcu.</li>
    <li><svg width="11" height="9" viewBox="0 0 11 9"><path d="M1 4.5 L4 7.5 L10 1" fill="none" stroke="#1aa3d9" stroke-width="2.2"/></svg><em>Donec commodo libero lorem.</em> Aliquam tellus leo, aliquet a porttitor fermentum, bibendum laoreet erat. Proin iaculis luctus ultricies.</li>
    <li><svg width="11" height="9" viewBox="0 0 11 9"><path d="M1 4.5 L4 7.5 L10 1" fill="none" stroke="#1aa3d9" stroke-width="2.2"/></svg><em>Mauris in augue tellus, id luctus magna.</em> Nulla tempor vehicula fringilla. Nunc nec felis vitae leo facilisis dapibus. Nam eget urna nec orci varius imperdiet.</li>
  </ul>
  <p>Mauris et velit leo. Nulla sem ligula, accumsan non tincidunt non, blandit eget elit. Ut auctor tellus id mauris malesuada eget interdum dolor tincidunt. Nunc eget augue a turpis venenatis euismod. Integer ultrices cursus diam et pharetra. Quisque sed est ante. Integer nunc mi, accumsan quis pretium vitae, vulputate sed leo. Aenean porttitor nisi sollicitudin diam rutrum vel suscipit mauris commodo.</p>
</article>

<section class="highlights">
  <div class="highlight" style="left:0">
    <svg class="marker" width="26" height="40" viewBox="0 0 26 40"><path d="M0 0 H26 V6 Q26 18 14 20 V40 H12 V20 Q0 18 0 6 Z" fill="#c6c6c6"/></svg>
    <h2>22 years experience<br>with big brands</h2>
    <p>Lorem ipsum dolor sit amet, consectetur adipiscing elit. Aliquam id nisi nisi. Sed non erat nisi. Nam tincidunt diam ultrices tellus hendrerit vehicula vel sit amet.</p>
    <div class="read-more" style="left:170px">READ MORE</div>
  </div>
  <div class="highlight" style="left:316px">
    <svg class="marker" width="26" height="40" viewBox="0 0 26 40"><path d="M0 0 H26 V6 Q26 18 14 20 V40 H12 V20 Q0 18 0 6 Z" fill="#c6c6c6"/></svg>
    <h2>Marketing your drink<br>the next big brand</h2>
    <p>Lorem ipsum dolor sit amet, consectetur adipiscing elit. Aliquam id nisi nisi. Sed non erat nisi. Nam tincidunt diam ultrices tellus hendrerit vehicula vel sit amet.</p>
    <div class="read-more" style="left:170px">READ MORE</div>
  </div>
  <div class="highlight third" style="left:630px">
    <svg class="marker" width="26" height="40" viewBox="0 0 26 40"><path d="M0 0 H26 V6 Q26 18 14 20 V40 H12 V20 Q0 18 0 6 Z" fill="#c6c6c6"/></svg>
    <h2>350 outlets that<br>listen to what we say</h2>
    <p>Lorem ipsum dolor sit amet, consectetur adipiscing elit. Aliquam id nisi nisi. Sed non erat nisi. Nam tincidunt diam ultrices tellus hendrerit vehicula vel sit amet.</p>
    <div class="read-more" style="left:171px">READ MORE</div>
  </div>
</section>

<footer class="site-footer">
  <div class="keyword-links">Brand Marketing <span>|</span> Brand Marketing Strategy <span>|</span> Drinks Marketing <span>|</span> Spirits Marketing <span>|</span> Alcohol Drinks Marketing <span>|</span> Drinks Brand Development</div>
  <div class="legal">© 1999 - 2010 Proof &amp; Palate | Terms &amp; Conditions | Privacy Policy</div>
</footer>

</body>
</html>
```